Stationery Refresh For Local Mortgage Broker

We want to modernise and standardise our stationery, including: letterhead, presentation folder, email signature and business card.

The new stationery should be a more modern and professional take on our existing colour scheme and brand. (We do not want a complete overhaul.) A folder of approved stock photos can be found here: https://filebox.example-share.net/f/7kQzR2mTn4vWx9Lp3Yb8-HsdJe5Uc1Ga/view

Our current website is: www.brindlecovefin.com.au but we will be updating this to be consistent with our new stationery.

We are open to *very slight* tweaks to our logo if you feel it needs modernising, but overall we would like to maintain consistent colour scheme.

> Letterhead

148 Calloway Parade,
Geelong, VIC, 3220
ABN: 31 805 249 067
Australian Credit License: 718293

(03) 5391 6084
www.brindlecovefin.com.au

> Presentation Folder

148 Calloway Parade,
Geelong, VIC, 3220
(03) 5391 6084
www.brindlecovefin.com.au

ABN: 31 805 249 067

> Email Signature

Liam Tresidder
Director
M. 0412 857 294
P. (03) 5391 6084
www.brindlecovefin.com.au
148 Calloway Parade,
Geelong, VIC, 3220

ABN: 31 805 249 067

(you can also include a photo if you like: https://brindlecovefin.com.au/wp-content/uploads/2020/12/Liam-Tresidder.png.webp)

> Business Card

Liam Tresidder
Director
M. 0412 857 294
P. (03) 5391 6084
www.brindlecovefin.com.au
148 Calloway Parade,
Geelong, VIC, 3220

ABN: 31 805 249 067

Additional information...

If it's useful/relevant, the services we offer are: Home Loans, Investment Loans, Refinance, Debt Consolidation, Commercial Finance, Vehicle Loans
(You may choose to use this in any of the designs)

Target Market(s)

Home Buyers and Investors

Industry/Entity Type

Mortgage broking/property/real estate

Requirements
Must have
• At least somewhat consistent with our current site (yet meaningfully modernized)
Should not have
• dramatically different logo or colourscheme overhauls

```html
<!DOCTYPE html>
<html lang="en">
<head>
<meta charset="utf-8">
<title>Brindle Cove Financial Services – Business Card</title>
<link rel="stylesheet" href="https://fonts.googleapis.com/css2?family=Montserrat:wght@400;500&family=Mulish:wght@400;500&display=swap">
<style>
  :root {
    --backdrop: #dcdcdc;
    --paper: #ffffff;
    --brand-red: #a8141c;
    --brand-red-light: #bd2733;
    --brand-red-dark: #9c0f17;
    --divider-grey: #7d7d7d;
    --slate-top: #8e8e8e;
    --slate-bottom: #626262;
    --slate-text: #e2e2e2;
    --ink-light: #ffffff;
  }
  * { margin: 0; padding: 0; box-sizing: border-box; }
  html, body { width: 1200px; height: 1200px; overflow: hidden; }
  body { background: var(--backdrop); position: relative; font-family: "Mulish", sans-serif; }

  .card-front { position: absolute; left: 262px; top: 165px; width: 686px; height: 392px; display: flex; }
  .card-front__brand {
    width: 335px; height: 100%; background: var(--paper);
    display: flex; align-items: center; justify-content: center;
  }
  .wordmark {
    font-family: "Montserrat", sans-serif; font-weight: 400;
    color: var(--brand-red); font-size: 25px; letter-spacing: 0.3em;
    margin-right: -0.3em; margin-top: -40px;
  }
  .card-front__divider { width: 8px; height: 100%; background: var(--divider-grey); }
  .card-front__details {
    flex: 1; height: 100%; color: var(--ink-light);
    background: linear-gradient(160deg, var(--brand-red-light) 0%, var(--brand-red) 45%, var(--brand-red-dark) 100%);
    padding: 66px 0 0 44px; position: relative;
  }
  .holder-name { font-size: 22px; font-weight: 400; letter-spacing: 0.01em; line-height: 1; }
  .holder-role { font-size: 15px; margin-top: 5px; line-height: 1; }
  .rule { width: 216px; height: 1px; background: var(--ink-light); opacity: 0.85; }
  .rule--top { margin-top: 15px; }
  .rule--bottom { margin-top: 14px; }
  .contact-list { list-style: none; margin-top: 14px; font-size: 15px; line-height: 19.6px; }
  .contact-list li { display: flex; align-items: flex-start; }
  .contact-icon { width: 14px; height: 19.6px; display: flex; align-items: center; justify-content: center; margin-right: 6px; flex: none; }
  .contact-icon svg { width: 12px; height: 12px; fill: var(--ink-light); }
  .contact-sep { margin-right: 5px; opacity: 0.9; }
  .licence { margin-top: 11px; font-size: 15px; line-height: 19.6px; }

  .card-back {
    position: absolute; left: 262px; top: 653px; width: 686px; height: 391px;
    background: linear-gradient(180deg, var(--slate-top) 0%, #7a7a7a 45%, var(--slate-bottom) 100%);
  }
  .card-back__name {
    position: absolute; top: 145px; left: 0; width: 100%; text-align: center;
    font-family: "Montserrat", sans-serif; font-weight: 400; font-size: 50px;
    letter-spacing: 0.14em; color: var(--slate-text); line-height: 1;
    text-indent: 0.14em;
  }
  .card-back__url {
    position: absolute; top: 327px; left: 0; width: 100%; text-align: center;
    font-family: "Montserrat", sans-serif; font-size: 15px; letter-spacing: 0.5em;
    text-indent: 0.5em; color: var(--slate-text);
  }
</style>
</head>
<body>
  <section class="card-front">
    <div class="card-front__brand">
      <div class="wordmark">BRINDLE COVE</div>
    </div>
    <div class="card-front__divider"></div>
    <div class="card-front__details">
      <h1 class="holder-name">LIAM TRESIDDER</h1>
      <p class="holder-role">Director</p>
      <div class="rule rule--top"></div>
      <ul class="contact-list">
        <li><span class="contact-icon"><svg viewBox="0 0 24 24"><path d="M6.6 10.8a15.2 15.2 0 0 0 6.6 6.6l2.2-2.2c.3-.3.7-.4 1-.2 1.1.4 2.3.6 3.6.6.6 0 1 .4 1 1V20c0 .6-.4 1-1 1A17 17 0 0 1 3 4c0-.6.4-1 1-1h3.5c.6 0 1 .4 1 1 0 1.3.2 2.5.6 3.6.1.3 0 .7-.2 1z"/></svg></span><span class="contact-sep">|</span>(03) 5391 6084</li>
        <li><span class="contact-icon"><svg viewBox="0 0 24 24"><path d="M7 1h10a2 2 0 0 1 2 2v18a2 2 0 0 1-2 2H7a2 2 0 0 1-2-2V3a2 2 0 0 1 2-2zm0 3v15h10V4z"/></svg></span><span class="contact-sep">|</span>0412 857 294</li>
        <li><span class="contact-icon"><svg viewBox="0 0 24 24"><path d="M2 5h20v14H2zm2 2v.5l8 5 8-5V7z"/></svg></span><span class="contact-sep">|</span>liam@brindlecovefin.com.au</li>
        <li><span class="contact-icon"><svg viewBox="0 0 24 24"><path d="M12 2a10 10 0 1 0 0 20 10 10 0 0 0 0-20zm-1 17.9A8 8 0 0 1 4.1 11H8v2l3 3zm6.9-2.5A2 2 0 0 0 16 16h-1v-3H9v-2h2V8h2V6h2.5a8 8 0 0 1 2.4 11.4z"/></svg></span><span class="contact-sep">|</span>brindlecovefin.com.au</li>
        <li><span class="contact-icon"><svg viewBox="0 0 24 24"><path d="M12 1a8 8 0 0 0-8 8c0 6 8 14 8 14s8-8 8-14a8 8 0 0 0-8-8zm0 11a3 3 0 1 1 0-6 3 3 0 0 1 0 6z"/></svg></span><span class="contact-sep">|</span><span>148 Calloway Parade<br>geelong, VIC, 3220</span></li>
      </ul>
      <div class="rule rule--bottom"></div>
      <p class="licence">Australian Credit Lic: 718293<br>ABN: 31 805 249 067</p>
    </div>
  </section>

  <section class="card-back">
    <div class="card-back__name">BRINDLE COVE</div>
    <div class="card-back__url">WWW.BRINDLECOVEFIN.COM.AU</div>
  </section>
</body>
</html>
```